I need a wordpress website for myconsulting company specialized in data privacy

I'm looking for a wordpress website for my consulting company specialized in data privacy (GDPR) and computer science.
The website will serve as entry point to for potential clients.
The website should have the following sections (I'm opened to new ideas):
- Presentation of the company
- General presentation
- Services provided with some details
- Blog/articles with tags (if possible)
- Contact
On every page of the website there should be some references to pages (such as privacy policy, legal information...)
If possible he website should be multinlingual (english and french). I'll personnally take care of the translation in french.
Regarding branding;
- Name of the company: Étienne Roubaud Conseil
- Logo is attached
- For colors to be used see attached PDF for exemple

```html
<!DOCTYPE html>
<html lang="en">
<head>
<meta charset="utf-8">
<title>Étienne Roubaud Conseil</title>
<link href="https://fonts.googleapis.com/css2?family=Russo+One&family=Roboto:wght@400;500;700&display=swap" rel="stylesheet">
<style>
:root{
  --navy:#0c3550;
  --navy-deep:#082a40;
  --teal:#0b7c8e;
  --teal-mid:#0f5f78;
  --grey-bg:#efefef;
  --text:#6d6d6d;
  --ink:#1e1e1e;
  --white:#ffffff;
}
*{margin:0;padding:0;box-sizing:border-box}
html,body{width:1200px;height:4007px;overflow:hidden}
body{position:relative;font-family:"Roboto",sans-serif;color:var(--text);background:var(--white)}
.abs{position:absolute}
.heading{font-family:"Russo One",sans-serif;color:var(--navy);font-weight:400}
.btn{position:absolute;display:flex;align-items:center;justify-content:center;gap:8px;border-radius:30px;font-weight:700;font-size:15px;text-transform:uppercase}
.dot{width:13px;height:13px;border-radius:50%;background:currentColor;position:relative}
.dot::after{content:"";position:absolute;left:4px;top:3.5px;border-left:5px solid var(--white);border-top:3px solid transparent;border-bottom:3px solid transparent}
.btn-light .dot::after,.dark-card .dot::after{border-left-color:var(--navy)}
.card-dark .dot::after{border-left-color:var(--teal)}

/* header */
.brand{position:absolute;display:flex;flex-direction:column;align-items:center;color:var(--navy)}
.brand .mark{width:40px;height:40px;border:5px solid var(--teal);margin-bottom:8px}
.brand .name{font-family:"Roboto",sans-serif;font-weight:500;font-size:23px;letter-spacing:1px;color:var(--navy)}
.nav{position:absolute;top:28px;left:448px;display:flex;gap:30px;font-size:15px;color:var(--ink);align-items:center}
.nav .active{color:var(--teal)}
.lang{display:flex;align-items:center;gap:7px}
.lang i{width:16px;height:16px;border-radius:50%;background:#c9cdd6;display:block}
.nav-cta{position:absolute;left:948px;top:20px;width:140px;height:37px;border-radius:20px;background:linear-gradient(90deg,var(--teal),var(--navy));color:var(--white);font-size:15px;font-weight:500;display:flex;align-items:center;justify-content:center}

/* hero */
.hero-title{left:109px;top:270px;font-size:50px;line-height:55px;color:var(--white)}
.hero-text{left:110px;top:403px;width:470px;font-size:16px;line-height:27px;color:var(--white);font-weight:500}
.btn-light{background:var(--white);color:var(--navy)}

/* welcome */
.welcome{left:0;top:724px;width:1200px;height:366px;background:var(--grey-bg)}
.center{text-align:center;width:1200px;left:0}
.kicker{top:778px;font-size:20px;font-weight:500;color:var(--teal)}
.welcome-title{top:808px;font-size:48px}
.welcome-text{left:130px;width:940px;top:880px;font-size:14px;line-height:26px;text-align:center}
.btn-outline{border:2px solid var(--teal);color:var(--teal);background:transparent}

/* about */
.about-frame{left:95px;top:1323px;width:345px;height:270px;border:4px solid var(--navy);border-top:none;border-right:none}
.about-frame::after{content:"";position:absolute;right:0;bottom:-4px;width:4px;height:14px;background:var(--navy)}
.about-img{left:114px;top:1173px;width:464px;height:400px;background:linear-gradient(135deg,#0d4a78,#0a2c4d 60%,#1c6aa3);box-shadow:0 6px 14px rgba(0,0,0,.25);border:2px solid var(--white)}
.about-title{left:644px;top:1188px;font-size:48px}
.about-text{left:644px;width:446px;font-size:14px;line-height:26.5px;text-align:justify}
.btn-grad{background:linear-gradient(90deg,var(--teal),var(--navy));color:var(--white)}

/* services */
.services{left:0;top:1684px;width:1200px;height:631px;background:linear-gradient(180deg,#ececec,#e2e3e4)}
.section-title{font-size:48px}
.card{position:absolute;top:1828px;width:223px;height:413px;border-radius:112px;border:10px solid var(--navy);background:var(--white)}
.card .side{position:absolute;top:90px;width:14px;height:205px;background:#e7e7e8}
.card .side.l{left:-12px}
.card .side.r{right:-12px}
.card .inner{position:absolute;inset:0 8px;border-radius:100px;background:var(--white)}
.card .icon{position:absolute;left:50%;top:45px;width:96px;height:96px;margin-left:-48px;border-radius:50%;background:var(--navy)}
.card h3{position:absolute;top:178px;width:100%;text-align:center;font-size:18px;font-weight:500;color:var(--ink)}
.card p{position:absolute;top:212px;left:18px;right:18px;text-align:center;font-size:13px;line-height:21.5px}
.card .more{position:absolute;top:330px;width:100%;display:flex;justify-content:center;align-items:center;gap:7px;font-size:15px;font-weight:700;color:var(--teal)}
.card.teal{border-color:var(--teal)}
.card.teal .icon{background:var(--teal)}
.card.black{border-color:#111}
.card.black .icon{background:#111}
.card-dark{border-color:#55595c}
.card-dark .inner{background:linear-gradient(180deg,var(--teal-mid),var(--teal))}
.card-dark .icon{background:#5a6166}
.card-dark h3,.card-dark p,.card-dark .more{color:var(--white)}

/* blog */
.post{position:absolute;top:2474px;width:310px;height:415px;background:var(--white);box-shadow:0 2px 12px rgba(0,0,0,.1)}
.post .thumb{height:207px;background:linear-gradient(135deg,#1b3b52,#4e6f86)}
.post:nth-of-type(2) .thumb{background:linear-gradient(135deg,#c9d2d8,#6e7b86)}
.post .date{position:absolute;top:14px;right:16px;width:45px;height:42px;background:var(--teal);color:var(--white);font-size:11px;font-weight:700;line-height:15px;text-align:center;padding-top:6px;border-radius:3px}
.post .meta{position:absolute;top:232px;left:20px;font-size:13px;color:#8a8a8a;display:flex;gap:6px;align-items:center}
.post .meta i{width:10px;height:10px;background:#8a8a8a;display:block}
.post h4{position:absolute;top:255px;left:20px;right:16px;font-size:17px;line-height:24px;color:var(--ink);font-weight:500}
.post p{position:absolute;top:310px;left:20px;right:16px;font-size:14px;line-height:24px}
.post .more{position:absolute;top:372px;left:20px;display:flex;gap:7px;align-items:center;font-size:14px;font-weight:700;color:var(--teal)}

/* contact */
.contact-title{top:3090px;font-size:44px;color:var(--white)}
.field{position:absolute;left:170px;width:418px;height:53px;border:1.5px solid rgba(255,255,255,.55);border-radius:27px;background:rgba(255,255,255,.08);color:var(--white);font-size:13px;padding:0 24px;display:flex;align-items:center}
.message{left:608px;top:3179px;width:423px;height:256px;border:1.5px solid rgba(255,255,255,.55);border-radius:26px;background:rgba(255,255,255,.08);color:var(--white);font-size:13px;padding:22px 28px}

/* footer */
.col-title{position:absolute;top:3710px;font-size:18px;font-weight:500;color:var(--ink)}
.links{position:absolute;top:3757px;list-style:none;font-size:13px;color:#6f6f6f}
.links li{height:33px;display:flex;gap:10px}
.links li::before{content:"»";color:var(--teal)}
.info{position:absolute;left:851px;top:3757px;list-style:none;font-size:13px;color:#6f6f6f;width:240px}
.info li{display:flex;gap:12px;line-height:23px;margin-bottom:10px}
.info i{flex:none;width:10px;height:10px;background:var(--teal);margin-top:7px;border-radius:2px}
.info i.pin{border-radius:50% 50% 50% 0;transform:rotate(-45deg)}
.social{position:absolute;top:3855px;width:37px;height:37px;border-radius:50%;background:#e4e4e4}
.rule{left:110px;top:3944px;width:980px;height:1px;background:#dedede}
.copy{top:3969px;font-size:13px;color:#6f6f6f}
.chat{left:1120px;top:3922px;width:36px;height:36px;border-radius:50%;background:var(--teal)}
</style>
</head>
<body>

<!-- hero shapes -->
<svg class="abs" style="left:0;top:0" width="1200" height="760" viewBox="0 0 1200 760">
  <defs>
    <linearGradient id="heroFill" x1="0" y1="0" x2="1" y2="1">
      <stop offset="0" stop-color="#0e6f86"/>
      <stop offset=".55" stop-color="#0c5475"/>
      <stop offset="1" stop-color="#0a7a8c"/>
    </linearGradient>
  </defs>
  <rect x="0" y="594" width="1200" height="140" fill="#efefef"/>
  <polygon role="img" aria-label="Photo of a business team at work, tinted in teal" fill="url(#heroFill)"
    points="0,121 372,121 420,78 1200,78 1200,594 772,594 650,704 0,704"/>
  <polygon fill="#0a7a8c" points="780,606 1200,602 1200,612 790,616"/>
  <polygon fill="#0c3550" points="0,712 652,712 774,604 790,612 662,724 0,724"/>
</svg>
<div class="abs" role="img" aria-label="Photo of smiling colleagues in an office" style="left:658px;top:137px;width:428px;height:400px;border-radius:22px;background:linear-gradient(135deg,#2a8ea0,#135a73 55%,#0d4a63);box-shadow:0 0 0 2px rgba(255,255,255,.25) inset"></div>

<!-- header -->
<div class="brand" style="left:109px;top:14px;width:242px">
  <span class="mark"></span>
  <span class="name">Étienne Roubaud</span>
</div>
<nav class="nav">
  <span class="active">Home</span><span>About</span><span>Our Services</span><span>Blog</span><span>Contact</span>
  <span class="lang"><i></i>Eng ▾</span>
</nav>
<div class="nav-cta">Contact us</div>

<h1 class="abs heading hero-title">Étienne Roubaud<br>Conseil</h1>
<p class="abs hero-text">Lorem ipsum dolor sit amet, consectetur adipiscing elit, sed do eiusmod tempor incididunt ut labore aliqua.</p>
<a class="btn btn-light" style="left:110px;top:482px;width:200px;height:50px">Learn more <span class="dot"></span></a>

<!-- welcome -->
<section class="abs welcome"></section>
<p class="abs center kicker">Welcome to</p>
<h2 class="abs center heading welcome-title">Étienne Roubaud Conseil</h2>
<p class="abs welcome-text">Sed ut perspiciatis unde omnis iste natus error sit voluptatem accusantium doloremque laudantium, totam rem aperiam, eaque ipsa quae ab illo inventore veritatis et quasi architecto beatae vitae dicta sunt explicabo. Nemo enim ipsam voluptatem quia voluptas sit aspernatur aut odit aut fugit, sed quia consequuntur magni dolores eos qui ratione voluptatem sequi nesciunt.</p>
<a class="btn btn-outline" style="left:512px;top:990px;width:178px;height:44px">Learn more <span class="dot"></span></a>

<!-- about -->
<div class="abs about-frame"></div>
<div class="abs about-img" role="img" aria-label="Illustration of hands typing on a keyboard with a glowing security shield"></div>
<h2 class="abs heading about-title">About Us</h2>
<p class="abs about-text" style="top:1264px">Lorem ipsum dolor sit amet, consectetur adipiscing elit, sed do eiusmod tempor incididunt ut labore et dolore magna aliqua. Ut enim ad minim veniam, quis nostrud exercitation ullamco laboris nisi ut aliquip ex ea commodo consequat.</p>
<p class="abs about-text" style="top:1383px">Sed ut perspiciatis unde omnis iste natus error sit voluptatem accusantium doloremque laudantium, totam rem aperiam, eaque ipsa sunt enim ipsam voluptatem quia voluptas explicabo.</p>
<a class="btn btn-grad" style="left:644px;top:1500px;width:195px;height:46px">Learn more <span class="dot"></span></a>

<!-- services -->
<section class="abs services"></section>
<h2 class="abs center heading section-title" style="top:1730px">Our Services</h2>

<div class="card" style="left:104px"><span class="side l"></span><span class="side r"></span><div class="inner"></div><span class="icon"></span><h3>Lorem amet</h3><p>Sed perspiciatis unde omnis iste natus error voluptatem accusantium eaque ipsa quae ab illo inventore veritatis</p><span class="more">Learn more <span class="dot"></span></span></div>
<div class="card teal" style="left:359px"><span class="side l"></span><span class="side r"></span><div class="inner"></div><span class="icon"></span><h3>Lorem amet</h3><p>Sed perspiciatis unde omnis iste natus error voluptatem accusantium eaque ipsa quae ab illo inventore veritatis</p><span class="more">Learn more <span class="dot"></span></span></div>
<div class="card card-dark" style="left:618px"><span class="side l"></span><span class="side r"></span><div class="inner"></div><span class="icon"></span><h3>Lorem amet</h3><p>Sed perspiciatis unde omnis iste natus error voluptatem accusantium eaque ipsa quae ab illo inventore veritatis</p><span class="more">Learn more <span class="dot"></span></span></div>
<div class="card black" style="left:873px"><span class="side l"></span><span class="side r"></span><div class="inner"></div><span class="icon"></span><h3>Lorem amet</h3><p>Sed perspiciatis unde omnis iste natus error voluptatem accusantium eaque ipsa quae ab illo inventore veritatis</p><span class="more">Learn more <span class="dot"></span></span></div>

<!-- blog -->
<h2 class="abs center heading section-title" style="top:2388px">Our Blog</h2>
<div>
<article class="post" style="left:110px"><div class="thumb" role="img" aria-label="Photo of a keyboard with a digital padlock"></div><span class="date">Feb 22<br>2022</span><span class="meta"><i></i>Lorem ipsum</span><h4>Sed ut perspiciatis unde omnis iste natus error sit voluptatem</h4><p>Lorem ipsum dolor sit amet, consectetur adipiscing elit, sed do eiusmod</p><span class="more">Read more <span class="dot"></span></span></article>
<article class="post" style="left:445px"><div class="thumb" role="img" aria-label="Photo of a team meeting around laptops"></div><span class="date">Feb 22<br>2022</span><span class="meta"><i></i>Lorem ipsum</span><h4>Sed ut perspiciatis unde omnis iste natus error sit voluptatem</h4><p>Lorem ipsum dolor sit amet, consectetur adipiscing elit, sed do eiusmod</p><span class="more">Read more <span class="dot"></span></span></article>
<article class="post" style="left:778px"><div class="thumb" role="img" aria-label="Photo of a hand holding a phone showing a secure login"></div><span class="date">Feb 22<br>2022</span><span class="meta"><i></i>Lorem ipsum</span><h4>Sed ut perspiciatis unde omnis iste natus error sit voluptatem</h4><p>Lorem ipsum dolor sit amet, consectetur adipiscing elit, sed do eiusmod</p><span class="more">Read more <span class="dot"></span></span></article>
</div>

<!-- contact -->
<svg class="abs" style="left:0;top:2960px" width="1200" height="690" viewBox="0 2960 1200 690">
  <defs>
    <linearGradient id="contactFill" x1="0" y1="0" x2="1" y2="1">
      <stop offset="0" stop-color="#0d7287"/>
      <stop offset=".5" stop-color="#0d5a76"/>
      <stop offset="1" stop-color="#0a3c5a"/>
    </linearGradient>
  </defs>
  <polygon fill="#0c3550" points="0,3078 420,3078 538,2980 1200,2980 1200,2990 544,2990 426,3088 0,3088"/>
  <polygon role="img" aria-label="Abstract network texture on a teal background" fill="url(#contactFill)"
    points="0,3093 428,3093 546,2995 1200,2995 1200,3522 790,3522 660,3628 0,3628"/>
  <polygon fill="#0a7a8c" points="0,3632 662,3632 790,3528 1200,3528 1200,3534 794,3534 666,3638 0,3638"/>
  <polygon fill="#0c3550" points="0,3642 668,3642 796,3538 810,3538 676,3652 0,3652"/>
</svg>
<h2 class="abs center heading contact-title">Contact Us</h2>
<div class="field" style="top:3179px">Name</div>
<div class="field" style="top:3247px">Email Address</div>
<div class="field" style="top:3314px">Phone Number</div>
<div class="field" style="top:3381px">Company</div>
<div class="abs message">Message</div>
<a class="btn btn-light" style="left:496px;top:3476px;width:207px;height:52px">Submit now <span class="dot"></span></a>

<!-- footer -->
<div class="brand" style="left:109px;top:3725px;width:272px">
  <span class="mark" style="width:52px;height:52px;border-width:6px"></span>
  <span class="name" style="font-size:25px">Étienne Roubaud</span>
</div>
<span class="social" style="left:162px"></span>
<span class="social" style="left:205px"></span>
<span class="social" style="left:248px"></span>
<span class="social" style="left:291px"></span>

<h5 class="col-title" style="left:462px">Quick Links</h5>
<ul class="links" style="left:462px"><li>Home</li><li>Services</li><li>Who We are</li><li>Careers</li><li>Contact</li></ul>
<h5 class="col-title" style="left:657px">Important</h5>
<ul class="links" style="left:657px"><li>Terms of Use</li><li>Site Map</li><li>Privacy Policy</li><li>Disclaimer</li></ul>
<h5 class="col-title" style="left:851px">Contact us</h5>
<ul class="info">
  <li><i class="pin"></i>1/155 Lorem ipsum dolor sit amet, consectetur adipiscing elit,</li>
  <li><i></i>+1 555 010 2040</li>
  <li><i></i>+1 555 010 3050</li>
  <li><i></i>info@roubaudconseil.example</li>
</ul>
<div class="abs rule"></div>
<p class="abs center copy">© 2022 Étienne Roubaud Conseil | All Rights Reserved</p>
<span class="abs chat"></span>

</body>
</html>
```